RK LAW
Stationary Envelopes and Cards
RK LAW - Law
Creative Brief
Professional
Howard P. Lindqvist
Attorney At Law
347 N. 4th Avenue Las Vegas NV 89104
nvrklaw@mailbrook.net
NVRKLAW.NET

```html
<!DOCTYPE html>
<html lang="en">
<head>
<meta charset="utf-8">
<title>RK LAW Stationery Set</title>
<link href="https://fonts.googleapis.com/css2?family=Open+Sans:wght@400;600;700&display=swap" rel="stylesheet">
<style>
:root{
  --blue:#1d5fa6;
  --blue-dark:#0f3d75;
  --blue-light:#5d9ad6;
  --ink:#333a44;
  --muted:#8a929c;
  --paper:#ffffff;
  --bg:#ffffff;
  --line:#c9d3de;
  --faint:#eef3f9;
}
*{box-sizing:border-box;margin:0;padding:0}
html,body{width:1200px;height:552px;overflow:hidden;background:var(--bg)}
body{position:relative;font-family:"Open Sans",Arial,sans-serif;color:var(--ink)}
.sheet{position:absolute;background:var(--paper);box-shadow:0 1px 4px rgba(0,0,0,.25);overflow:hidden}
.brand{font-family:"Open Sans",Arial,sans-serif;font-weight:600;color:var(--blue);display:flex;align-items:center;gap:5px;line-height:1;white-space:nowrap}
.brand .mark{display:inline-block;background:var(--blue)}
.stripe{position:absolute;left:0;top:0;bottom:0;width:6px;background:linear-gradient(var(--blue-light),var(--blue-dark))}
.body-text{font-size:5.2px;line-height:7.4px;color:var(--ink)}
.body-text p{margin-bottom:6px}
.sign{font-size:5.2px;line-height:7px}
.signature{width:46px;height:12px;margin:3px 0;background:linear-gradient(90deg,#dfe7f1,#b7c8dc);border-radius:6px}

/* Fax sheet */
.fax{left:19px;top:19px;width:360px;height:514px}
.fax .brand{position:absolute;left:20px;top:16px;font-size:13px}
.fax .brand .mark{width:8px;height:8px}
.fax-title{position:absolute;right:18px;top:52px;font-size:8px;font-weight:700;color:var(--ink)}
.fax-table{position:absolute;left:20px;top:62px;width:322px;border-collapse:collapse;font-size:5.6px}
.fax-table td{border:1px solid var(--line);height:11px;padding:0 3px;width:25%}
.fax-table td.lbl{color:var(--muted);width:14%}
.fax-checks{position:absolute;left:20px;top:124px;width:322px;display:flex;justify-content:space-between;font-size:5.6px;color:var(--ink)}
.fax-checks span::before{content:"";display:inline-block;width:5px;height:5px;border:1px solid var(--muted);margin-right:3px;vertical-align:-1px}
.fax .body-text{position:absolute;left:20px;top:140px;width:322px}
.fax .sign{position:absolute;left:20px;top:440px}
.fax-foot{position:absolute;left:20px;right:18px;bottom:14px;border-top:1px solid var(--blue);padding-top:3px;font-size:4.8px;color:var(--muted);display:flex;justify-content:space-between}

/* Letterhead */
.letter{left:398px;top:19px;width:370px;height:514px}
.letter .brand{position:absolute;left:22px;top:16px;font-size:13px}
.letter .brand .mark{width:8px;height:8px}
.letter-contact{position:absolute;right:18px;top:16px;font-size:4.8px;line-height:6.6px;text-align:right;color:var(--muted)}
.recipient{position:absolute;left:22px;top:50px;font-size:5.2px;line-height:7px}
.letter .body-text{position:absolute;left:22px;top:82px;width:326px}
.letter .sign{position:absolute;left:22px;top:440px}
.watermark{position:absolute;right:20px;bottom:60px;font-family:"Open Sans",Arial,sans-serif;font-weight:600;font-size:44px;color:var(--faint);white-space:nowrap}
.letter-foot{position:absolute;left:22px;right:18px;bottom:14px;border-top:1px solid var(--blue);padding-top:3px;font-size:4.8px;color:var(--muted);display:flex;justify-content:space-between}

/* Business cards */
.card-front{left:792px;top:24px;width:180px;height:91px}
.card-front .brand{position:absolute;left:12px;top:14px;font-size:12px}
.card-front .brand .mark{width:7px;height:7px}
.card-front .title{position:absolute;left:12px;top:31px;font-size:5px;color:var(--muted);letter-spacing:.5px}
.card-front .person{position:absolute;right:10px;top:44px;text-align:right;font-size:4.8px;line-height:6.4px;color:var(--ink)}
.card-front .person strong{font-size:6px;color:var(--blue-dark)}
.card-front .band{position:absolute;left:0;right:0;bottom:0;height:6px;background:linear-gradient(90deg,var(--blue-dark),var(--blue-light))}
.card-back{left:989px;top:24px;width:192px;height:91px;background:radial-gradient(circle at 50% 40%,var(--blue-light),var(--blue-dark))}
.card-back .brand{position:absolute;left:50%;top:50%;transform:translate(-50%,-50%);font-size:16px;color:#fff}
.card-back .brand .mark{width:9px;height:9px;background:#fff}

/* Envelope */
.envelope{left:792px;top:283px;width:389px;height:245px}
.envelope .brand{position:absolute;left:16px;top:16px;font-size:14px}
.envelope .brand .mark{width:8px;height:8px}
.env-address{position:absolute;left:16px;top:36px;font-size:5px;line-height:6.8px;color:var(--muted)}
.env-wave{position:absolute;left:0;bottom:0;width:389px;height:70px}
</style>
</head>
<body>

<section class="sheet fax">
  <div class="stripe"></div>
  <div class="brand"><span class="mark"></span>RK LAW</div>
  <div class="fax-title">FAX</div>
  <table class="fax-table">
    <tr><td class="lbl">To:</td><td></td><td class="lbl">From:</td><td></td></tr>
    <tr><td class="lbl">Fax:</td><td></td><td class="lbl">Pages:</td><td></td></tr>
    <tr><td class="lbl">Phone:</td><td></td><td class="lbl">Date:</td><td></td></tr>
    <tr><td class="lbl">Re:</td><td></td><td class="lbl">CC:</td><td></td></tr>
  </table>
  <div class="fax-checks">
    <span>Urgent</span><span>For Review</span><span>Please Comment</span><span>Please Reply</span><span>Please Recycle</span>
  </div>
  <div class="body-text">
    <p>Please find attached the signed documents for the matter we discussed during our meeting last week. Kindly review each page carefully and confirm receipt at your earliest convenience so that our office can proceed with the filing before the court deadline.</p>
    <p>Should any detail require correction, mark the relevant section and return the pages by fax. Our staff will update the records promptly and send a revised copy for your final approval.</p>
    <p>We have also included a short schedule of the next steps, together with the dates on which your attendance may be required. Please keep this sheet with your records and let us know of any conflict as soon as possible.</p>
    <p>Thank you for your continued trust in our firm. We remain available by phone or email for any questions about this transmission.</p>
  </div>
  <div class="sign">
    Yours Sincerely,
    <div class="signature" role="img" aria-label="Handwritten signature"></div>
    Howard P. Lindqvist
  </div>
  <div class="fax-foot"><span>347 N. 4th Avenue Las Vegas NV 89104</span><span>nvrklaw@mailbrook.net</span><span>NVRKLAW.NET</span></div>
</section>

<section class="sheet letter">
  <div class="stripe"></div>
  <div class="brand"><span class="mark"></span>RK LAW</div>
  <div class="letter-contact">347 N. 4th Avenue Las Vegas NV 89104<br>(702) 555-0148<br>nvrklaw@mailbrook.net</div>
  <div class="recipient">Dana Whitfield<br>18 Harbor Lane<br>Reno NV 89501</div>
  <div class="body-text">
    <p>Dear Dana Whitfield,</p>
    <p>Please find attached the signed documents for the matter we discussed during our meeting last week. Kindly review each page carefully and confirm receipt at your earliest convenience so that our office can proceed with the filing before the court deadline.</p>
    <p>We have reviewed the proposed agreement and believe the terms are fair to both parties. A few clauses regarding payment schedules should be clarified before signing, and we have outlined those points in the enclosed summary.</p>
    <p>Should any detail require correction, mark the relevant section and return the pages by fax. Our staff will update the records promptly and send a revised copy for your final approval.</p>
    <p>We have also included a short schedule of the next steps, together with the dates on which your attendance may be required. Please keep this letter with your records and let us know of any conflict as soon as possible.</p>
    <p>Thank you for your continued trust in our firm. We remain available by phone or email for any questions about this letter.</p>
  </div>
  <div class="sign">
    Yours Sincerely,
    <div class="signature" role="img" aria-label="Handwritten signature"></div>
    Howard P. Lindqvist
  </div>
  <div class="watermark" aria-hidden="true">RK LAW</div>
  <div class="letter-foot"><span>Attorney At Law</span><span>NVRKLAW.NET</span></div>
</section>

<section class="sheet card-front">
  <div class="brand"><span class="mark"></span>RK LAW</div>
  <div class="title">ATTORNEY AT LAW</div>
  <div class="person"><strong>Howard P. Lindqvist</strong><br>347 N. 4th Avenue Las Vegas NV 89104<br>nvrklaw@mailbrook.net<br>NVRKLAW.NET</div>
  <div class="band"></div>
</section>

<section class="sheet card-back">
  <div class="brand"><span class="mark"></span>RK LAW</div>
</section>

<section class="sheet envelope">
  <div class="brand"><span class="mark"></span>RK LAW</div>
  <div class="env-address">347 N. 4th Avenue<br>Las Vegas NV 89104</div>
  <svg class="env-wave" viewBox="0 0 389 70" preserveAspectRatio="none" aria-hidden="true">
    <defs>
      <linearGradient id="waveFill" x1="0" x2="1">
        <stop offset="0" stop-color="#0f3d75"/>
        <stop offset="1" stop-color="#5d9ad6"/>
      </linearGradient>
    </defs>
    <path d="M0 30 C120 60 260 10 389 40 L389 70 L0 70 Z" fill="url(#waveFill)" opacity=".35"/>
    <path d="M0 45 C130 70 250 30 389 55 L389 70 L0 70 Z" fill="url(#waveFill)"/>
  </svg>
</section>

</body>
</html>
```